Information Technology Cloud Services Website

"Offer in every submission a high resolution version of your concept please. It is difficult to see of my text (sales copy) was added to your screenshot or not. It is necessary for me to provide high quality feedback."

My company provides a customizable ecosystem for Brindlewave Deskset 880 and Corvel users that includes all the technologies for organizing business processes and communications, letting my clients manage business without fear.

You can see our current site at http://www.DesksetShiftCrew.com

I currently use WordPress using the theme platform OptimizePress. If you have OptimizePress, that would be perfect, yet not required. However, I do need the finish product in WordPress for future additions and edits.

The Brand colors are Light Blue just like the logo attached.

I am in the need of graphic images on every webpage that can convey the services that my company does.

We need a refresh of our existing website that looks more 2018. We have made a mockup of the content that we want and a sample of where we want it. Nothing is set in stone, if you have better ideas of where things should go, feel free.

Here are some competitors similar sites we like - but still looking for a unique design that fits out brand

https://www.quorvatek.com/

https://www.tarnwell.com/email-migrations/deskset-880-shift-crew

https://www.gorvanta.com/solutions/mailbox-migration/

https://www.plumeridge.com/

https://www.plumeridge.com/deskset-880/

Target Market(s)

Business = IT Managers, IT Directors, IT Staff, IT Vice Presidents, Chief Information Officer

Industry/Entity Type

Information Technology

Coding

Coded - Design and coding required

Number of Pages Required

5+ page

Font styles to use
Sans Serif

Colors

Designer to choose colors to be used in the design.

Requirements
Must have
• Must have creative graphic images that convey the story/services that I offer. Its important to us that the design is very explanatory, the customer should easily be able to figure out that we provide Deskset 880 migrations services right away. Also we are looking for a new very responsive HTML5+ webpages in WordPress.

```html
<!DOCTYPE html>
<html lang="en">
<head>
<meta charset="utf-8">
<title>DesksetShiftCrew — Deskset 880 Migration Services</title>
<link rel="stylesheet" href="https://fonts.googleapis.com/css2?family=Poppins:wght@400;500;600;700&family=Open+Sans:wght@400;600;700&display=swap">
<style>
:root{
  --navy:#0c2d57;
  --navy-deep:#082244;
  --navy-card:#173f6e;
  --blue:#1e8fe1;
  --blue-bright:#2ea3f2;
  --ink:#2b3440;
  --muted:#6b7683;
  --paper:#ffffff;
  --mist:#f2f4f7;
  --footer:#1d1f23;
  --footer-text:#b9bec6;
}
*{margin:0;padding:0;box-sizing:border-box}
html,body{width:1200px;height:4511px;overflow:hidden}
body{position:relative;background:var(--paper);font-family:"Open Sans",Arial,sans-serif;color:var(--ink)}
.section{position:absolute;left:0;width:1200px}
h1,h2,h3,.nav a,.btn{font-family:"Poppins",Arial,sans-serif}

/* header / hero */
.hero{top:0;height:585px;overflow:hidden}
.hero-photo{position:absolute;inset:0;background:linear-gradient(100deg,#8ea0b4 0%,#5d7590 30%,#1f3c63 55%,#0d2b52 100%)}
.hero-shade{position:absolute;inset:0;background:linear-gradient(90deg,rgba(12,45,87,0) 35%,rgba(12,45,87,.55) 60%,rgba(8,34,68,.75) 100%)}
.brand-box{position:absolute;left:0;top:0;width:390px;height:96px;background:var(--navy);display:flex;align-items:center;padding-left:34px;gap:14px}
.brand-dot{width:44px;height:44px;border-radius:50%;background:var(--blue-bright)}
.brand-name{font-family:"Poppins",sans-serif;font-weight:600;font-size:19px;color:#fff}
.topline{position:absolute;right:30px;top:8px;font-size:14px;color:#fff;display:flex;align-items:center;gap:8px}
.nav{position:absolute;left:390px;top:30px;width:795px;height:60px;background:#fff;display:flex;align-items:center;padding-left:24px}
.nav a{font-size:15px;color:var(--ink);text-decoration:none;margin-right:36px;position:relative}
.nav a.active{font-weight:600;color:var(--navy)}
.nav a.active::after{content:"";position:absolute;left:0;right:0;bottom:-18px;height:3px;background:var(--blue)}
.nav .search{position:absolute;right:0;top:0;width:60px;height:60px;background:var(--mist);display:flex;align-items:center;justify-content:center}
.hero-copy{position:absolute;left:610px;top:185px;width:560px;color:#fff}
.hero-copy h1{font-size:27px;font-weight:700;line-height:1.32;text-transform:uppercase}
.hero-copy p{font-size:15px;margin-top:22px;line-height:1.5;color:#dbe6f2;width:320px}
.hero-actions{margin-top:18px;display:flex;gap:22px}
.btn{display:inline-block;background:var(--blue-bright);color:#fff;font-size:13px;font-weight:500;border-radius:22px;padding:10px 26px;text-decoration:none}
.hero-arrow{position:absolute;left:605px;top:546px}

/* media band */
.press{top:585px;height:115px;background:var(--navy-deep);display:flex;align-items:center;padding-left:172px;color:#fff}
.press-label{font-size:17px;margin-right:80px;font-family:"Poppins",sans-serif}
.press-name{font-family:"Poppins",sans-serif;font-weight:700;font-size:26px;margin-right:88px;color:#fff}

/* about */
.about{top:700px;height:590px}
.about-photo{position:absolute;left:171px;top:86px;width:420px;height:414px;background:linear-gradient(135deg,#c9d3dd,#8fa2b7 60%,#5a708a)}
.about-photo-inset{position:absolute;left:251px;top:146px;width:260px;height:220px;background:linear-gradient(135deg,#6f88a6,#2e4d78);border:6px solid #fff}
.about-text{position:absolute;left:609px;top:78px;width:505px;font-size:12.5px;line-height:1.75;color:var(--muted)}
.about-text h3{font-size:17px;font-weight:600;color:var(--navy);margin:14px 0 8px}
.about-text p{margin-bottom:10px}
.about-text b{color:var(--blue);font-weight:700}

/* process */
.process{top:1290px;height:630px;background:var(--mist)}
.section-title{text-align:center;font-size:36px;font-weight:600;color:var(--navy);font-family:"Poppins",sans-serif}
.section-title span{color:var(--blue)}
.process .section-title{margin-top:42px}
.section-sub{text-align:center;font-size:15px;color:var(--navy);letter-spacing:.5px;margin-top:4px;font-family:"Poppins",sans-serif}
.process-map{position:absolute;left:0;top:175px}
.step-note{position:absolute;left:171px;top:380px;width:168px;height:195px;background:var(--navy);color:#dbe6f2;font-size:11px;line-height:1.6;padding:18px 14px;text-align:center}

/* cta band */
.cta{top:1830px;height:390px}
.cta-band{position:absolute;left:0;top:90px;width:1200px;height:300px;background:var(--navy)}
.cta-photo{position:absolute;left:690px;top:0;width:390px;height:390px;border-radius:195px 195px 0 0;background:linear-gradient(160deg,#e9dccd,#c9b6a1 45%,#8d9fb3);overflow:hidden}
.cta-copy{position:absolute;left:171px;top:160px;width:470px;color:#fff}
.cta-copy h2{font-size:24px;font-weight:500;line-height:1.45}
.cta-copy .btn{margin-top:36px}

/* what we migrate */
.migrate{top:2220px;height:680px}
.migrate-photo{position:absolute;left:0;top:165px;width:570px;height:330px;border-radius:0 165px 165px 0;background:linear-gradient(120deg,#bcc8d6,#7d93ad 55%,#3b5678)}
.migrate .section-title{position:absolute;left:585px;top:172px;text-align:left}
.migrate-grid{position:absolute;left:585px;top:265px;width:480px;display:grid;grid-template-columns:240px 240px;row-gap:60px}
.item svg{display:block;margin-bottom:10px}
.item h3{font-size:14px;font-weight:600;color:var(--navy)}
.item p{font-size:11.5px;color:var(--muted);line-height:1.5;margin-top:4px;width:190px}

/* testimonials */
.voices{top:2900px;height:530px;background:linear-gradient(180deg,#123a6b,#0b2a52)}
.voices .section-title{color:#fff;font-size:30px;font-weight:500;margin-top:92px}
.voices .section-sub{color:#c5d3e4;font-size:14px;width:520px;margin:8px auto 0;line-height:1.5}
.quote{position:absolute;top:265px;width:268px;height:165px;background:var(--navy-card);padding:34px 22px 0;color:#c9d6e6}
.quote .avatar{position:absolute;left:50%;top:-26px;margin-left:-26px;width:52px;height:52px;border:3px solid #fff;background:linear-gradient(135deg,#8ba0b8,#3c5a80)}
.quote p{font-size:11px;line-height:1.6}
.quote h3{font-size:12.5px;font-weight:500;color:var(--blue-bright);margin-top:14px;text-align:center}
.quote small{display:block;text-align:center;font-size:10px;color:#9fb1c7;margin-top:2px}
.voices-arrows{position:absolute;left:545px;top:460px;display:flex;gap:40px}

/* form */
.lead{top:3430px;height:765px}
.form-card{position:absolute;left:171px;top:80px;width:430px;height:645px;background:#fff;box-shadow:0 6px 26px rgba(12,45,87,.14)}
.form-head{height:110px;background:var(--navy);text-align:center;padding-top:26px}
.form-head h2{font-size:18px;font-weight:600;color:#fff}
.form-head p{font-size:12.5px;color:var(--blue-bright);margin:6px auto 0;width:280px;line-height:1.45}
.field{margin:0 30px;height:64px;border-bottom:1px solid #dde2e8;display:flex;align-items:flex-end;padding-bottom:10px;font-size:13px;color:var(--ink)}
.form-card .btn{display:block;margin:38px auto 0;width:210px;text-align:center;background:var(--navy);font-size:12.5px}
.lead-circle{position:absolute;left:650px;top:240px;width:440px;height:440px;border-radius:50%;background:var(--navy)}
.lead-photo{position:absolute;left:640px;top:160px;width:390px;height:300px;border-radius:14px;background:linear-gradient(140deg,#f2f4f7,#c4cfdb 50%,#7f95b0);box-shadow:0 10px 30px rgba(0,0,0,.2)}

/* footer */
.footer{top:4195px;height:316px;background:var(--footer);color:var(--footer-text);font-size:12px}
.footer h3{font-size:14px;font-weight:500;color:#fff;margin-bottom:12px}
.col{position:absolute;top:40px;line-height:1.75}
.col ul{list-style:none}
.mini-field{width:330px;height:24px;border-bottom:1px solid #3a3e45;font-size:10px;display:flex;align-items:flex-end;padding-bottom:3px;margin-bottom:8px}
.mini-send{display:inline-block;background:var(--blue);color:#fff;font-size:10px;padding:4px 22px;margin-top:6px;margin-left:120px}
.copyright{position:absolute;left:0;right:0;top:255px;text-align:center;font-size:10px;line-height:1.6;color:#8e949c}
</style>
</head>
<body>

<header class="section hero">
  <div class="hero-photo" role="img" aria-label="Photo of a team working together at a laptop in a bright office"></div>
  <div class="hero-shade"></div>
  <div class="brand-box"><span class="brand-dot"></span><span class="brand-name">DesksetShiftCrew.com</span></div>
  <div class="topline">
    <svg width="14" height="14" viewBox="0 0 24 24"><path fill="#fff" d="M6.6 10.8a15 15 0 0 0 6.6 6.6l2.2-2.2c.3-.3.7-.4 1-.2 1.1.4 2.3.6 3.6.6.6 0 1 .4 1 1V20c0 .6-.4 1-1 1C10.6 21 3 13.4 3 4c0-.6.4-1 1-1h3.5c.6 0 1 .4 1 1 0 1.3.2 2.5.6 3.6.1.3 0 .7-.2 1z"/></svg>
    Call us: (877) 555-0148
  </div>
  <nav class="nav">
    <a class="active" href="#">Home</a>
    <a href="#">Email Migrations</a>
    <a href="#">Migration Solutions</a>
    <a href="#">Mergers</a>
    <a href="#">Technology Services</a>
    <a href="#">About Us</a>
    <span class="search"><svg width="18" height="18" viewBox="0 0 24 24"><circle cx="10" cy="10" r="6.5" fill="none" stroke="#0c2d57" stroke-width="2.2"/><path d="M15 15l6 6" stroke="#0c2d57" stroke-width="2.2"/></svg></span>
  </nav>
  <div class="hero-copy">
    <h1>Are you willing to cut costs &amp; boost productivity by migrating your email server &amp;infrastructure to the cloud?</h1>
    <p>We Help Companies Quickly and Professionally Migrate To Deskset 880 &amp; Corvel</p>
    <div class="hero-actions"><a class="btn" href="#">Request a Quote</a><a class="btn" href="#">Learn More</a></div>
  </div>
  <svg class="hero-arrow" width="26" height="14" viewBox="0 0 26 14"><path d="M1 7h22M17 1l6 6-6 6" fill="none" stroke="#fff" stroke-width="2"/></svg>
</header>

<section class="section press">
  <span class="press-label">As Seen In:</span>
  <span class="press-name">Vantlow</span>
  <span class="press-name">Orbridge</span>
  <span class="press-name">Kestrel News</span>
  <span class="press-name">Meridale</span>
</section>

<section class="section about">
  <div class="about-photo" role="img" aria-label="Collage of office workers collaborating around computers"></div>
  <div class="about-photo-inset" role="img" aria-label="Two colleagues reviewing data on a monitor"></div>
  <div class="about-text">
    <p>When it comes to migrating your email server, apps or infrastructure to the cloud, you don't have to lose sleep or spend over your budget. All you have to do is choose DesksetShiftCrew and we will professionally and efficiently handle every single detail.</p>
    <h3>Here's How DesksetShiftCrew Can Help Your Business</h3>
    <p><b>SAVE TIME</b> - Our team of experts will determine your needs and develop a 100% custom migration strategy tailored to your company. We will analyze your current environment and prepare your Deskset 880 profiles and users. You do not have to trouble yourself with all the technical details anymore.</p>
    <p><b>SAVE EFFORT</b> - After identifying your needs, we will start migrating your data. Your email service will be re-routed to Deskset 880 and we will help you set up the new email service on all your local desktops and mobile devices. Once the migration process is complete, we will review the results and ensure that everything went according to plan.</p>
    <p><b>SAVE MONEY</b> - Migrating your data to Deskset 880 means cutting down all expenses and boosting your performance. Plus, we offer you flexible monthly licenses, so you are not stuck with upfront annual contract license costs.</p>
  </div>
</section>

<section class="section process">
  <h2 class="section-title">OUR <span>MIGRATION</span> PROCESS</h2>
  <p class="section-sub">AT ANY TIME OF THE DAY OR NIGHT, 24/7 &amp; 365 DAYS OUT OF THE YEAR</p>
  <svg class="process-map" width="1200" height="240" viewBox="0 0 1200 240" font-family="Poppins, sans-serif">
    <defs>
      <marker id="head" viewBox="0 0 10 10" refX="5" refY="5" markerWidth="6" markerHeight="6" orient="auto"><path d="M0 0L10 5L0 10z" fill="#0c2d57"/></marker>
    </defs>
    <g fill="none" stroke="#0c2d57" stroke-width="3" marker-end="url(#head)">
      <path d="M255 60 C255 0 426 0 426 55"/>
      <path d="M426 60 C426 0 600 0 600 55"/>
      <path d="M600 60 C600 0 771 0 771 55"/>
      <path d="M771 60 C771 0 939 0 939 55"/>
    </g>
    <g>
      <circle cx="255" cy="125" r="66" fill="#0c2d57"/><path d="M189 125a66 66 0 0 0 132 0z" fill="#1e8fe1"/>
      <circle cx="255" cy="125" r="48" fill="#fff"/>
      <text x="255" y="112" text-anchor="middle" font-size="12" fill="#1e8fe1">First</text>
      <text x="255" y="127" text-anchor="middle" font-size="12" fill="#1e8fe1">Contact</text>
      <path d="M243 140h24v10h-24z" fill="none" stroke="#0c2d57" stroke-width="2"/>
    </g>
    <g>
      <circle cx="426" cy="125" r="66" fill="#0c2d57"/><path d="M360 125a66 66 0 0 0 132 0z" fill="#1e8fe1"/>
      <circle cx="426" cy="125" r="48" fill="#fff"/>
      <text x="426" y="112" text-anchor="middle" font-size="12" fill="#1e8fe1">Pre</text>
      <text x="426" y="127" text-anchor="middle" font-size="12" fill="#1e8fe1">Migration</text>
      <path d="M414 150a8 8 0 0 1 2-14a10 10 0 0 1 19 2a6 6 0 0 1 1 12z" fill="#1e8fe1"/>
    </g>
    <g>
      <circle cx="600" cy="125" r="66" fill="#0c2d57"/><path d="M534 125a66 66 0 0 0 132 0z" fill="#0c2d57"/>
      <circle cx="600" cy="125" r="48" fill="#fff"/>
      <text x="600" y="112" text-anchor="middle" font-size="12" fill="#1e8fe1">Start</text>
      <text x="600" y="127" text-anchor="middle" font-size="12" fill="#1e8fe1">Migration</text>
      <rect x="588" y="137" width="24" height="16" rx="2" fill="none" stroke="#0c2d57" stroke-width="2"/>
    </g>
    <g>
      <circle cx="771" cy="125" r="66" fill="#0c2d57"/><path d="M705 125a66 66 0 0 0 132 0z" fill="#1e8fe1"/>
      <circle cx="771" cy="125" r="48" fill="#fff"/>
      <text x="771" y="112" text-anchor="middle" font-size="12" fill="#1e8fe1">Local</text>
      <text x="771" y="127" text-anchor="middle" font-size="12" fill="#1e8fe1">Setup</text>
      <path d="M759 137h24v12h-24zM765 152h12" fill="none" stroke="#0c2d57" stroke-width="2"/>
    </g>
    <g>
      <circle cx="939" cy="125" r="66" fill="#0c2d57"/><path d="M873 125a66 66 0 0 0 132 0z" fill="#1e8fe1"/>
      <circle cx="939" cy="125" r="48" fill="#fff"/>
      <text x="939" y="112" text-anchor="middle" font-size="12" fill="#1e8fe1">Post</text>
      <text x="939" y="127" text-anchor="middle" font-size="12" fill="#1e8fe1">Migration</text>
      <path d="M929 145l7 7 13-14" fill="none" stroke="#1e8fe1" stroke-width="2.5"/>
    </g>
  </svg>
  <div class="step-note">Our team of experts will contact you to determine your needs and develop a custom migration strategy. A dedicated migration agent will be assigned to your account as the main contact for the whole migration process.</div>
</section>

<section class="section cta">
  <div class="cta-band"></div>
  <div class="cta-photo" role="img" aria-label="Photo of a smiling woman working on a laptop"></div>
  <div class="cta-copy">
    <h2>Cloud Services Like Brindlewave Deskset 880 And Corvel Can Help You Boost Your Productivity? Speak With One Of Our Expert Engineers About Your Business Goals</h2>
    <a class="btn" href="#">Request a Quote Today!</a>
  </div>
</section>

<section class="section migrate">
  <div class="migrate-photo" role="img" aria-label="Photo of a business team in a meeting around a table"></div>
  <h2 class="section-title">WHAT WE <span>MIGRATE</span></h2>
  <div class="migrate-grid">
    <div class="item">
      <svg width="28" height="28" viewBox="0 0 28 28"><rect x="4" y="3" width="18" height="22" rx="2" fill="none" stroke="#0c2d57" stroke-width="2"/><path d="M9 10h8M9 15h8M9 20h5" stroke="#1e8fe1" stroke-width="2"/></svg>
      <h3>Userbase Directory Synchronization</h3>
      <p>No Need To Recreate Your Directory</p>
    </div>
    <div class="item">
      <svg width="28" height="28" viewBox="0 0 28 28"><rect x="3" y="7" width="22" height="15" rx="2" fill="none" stroke="#0c2d57" stroke-width="2"/><path d="M3 8l11 8 11-8" fill="none" stroke="#1e8fe1" stroke-width="2"/></svg>
      <h3>Mailboxes</h3>
      <p>All Email And Data From Virtually All Email Platforms</p>
    </div>
    <div class="item">
      <svg width="28" height="28" viewBox="0 0 28 28"><path d="M8 21a6 6 0 0 1 1-12 8 8 0 0 1 15 3 4.5 4.5 0 0 1-1 9z" fill="none" stroke="#0c2d57" stroke-width="2"/><path d="M14 12v8M11 17l3 3 3-3" fill="none" stroke="#1e8fe1" stroke-width="2"/></svg>
      <h3>Data Storage</h3>
      <p>Data Storage to CloudLocker Cloud Storage</p>
    </div>
    <div class="item">
      <svg width="28" height="28" viewBox="0 0 28 28"><circle cx="9" cy="14" r="4" fill="none" stroke="#0c2d57" stroke-width="2"/><circle cx="21" cy="7" r="3.5" fill="none" stroke="#1e8fe1" stroke-width="2"/><circle cx="21" cy="21" r="3.5" fill="none" stroke="#1e8fe1" stroke-width="2"/><path d="M12.5 12l5.5-3.5M12.5 16l5.5 3.5" stroke="#0c2d57" stroke-width="2"/></svg>
      <h3>DocuVault</h3>
      <p>From DocuVault To DocuVault Online</p>
    </div>
  </div>
</section>

<section class="section voices">
  <h2 class="section-title">JOIN 1000'S OF PEOPLE BENEFITING FROM DESKSET 880</h2>
  <p class="section-sub">Lorem ipsum dolor sit amet, consectetur adipiscing elit. Aenean accumsan dolor dolor, in pulvinar porttitor velit in pharetra.</p>
  <div class="quote" style="left:171px">
    <div class="avatar" role="img" aria-label="Portrait photo of the client"></div>
    <p>Deskset 880 is much more than just email. It's a cloud offering that provides a whole range of communication and collaboration services that will help us stay current and optimized for success. Our subscription</p>
    <h3>Dale Merriton, Chief Technology Officer</h3><small>Norvale</small>
  </div>
  <div class="quote" style="left:466px">
    <div class="avatar" role="img" aria-label="Portrait photo of the client"></div>
    <p>With Deskset 880, maintenance employees anywhere on the rail network can access the emails that they need to help operate the railroad. Inefficiency is a long-cost chore, their manuals online, and marketing step.</p>
    <h3>Renna Holcombe, Chief Information</h3><small>Brookline Railway</small>
  </div>
  <div class="quote" style="left:757px">
    <div class="avatar" role="img" aria-label="Portrait photo of the client"></div>
    <p>Deskset 880 is much more than just email. It's a cloud offering that provides a whole range of communication and collaboration services that will help us stay current and optimized for success. Our subscription</p>
    <h3>Dale Merriton, Chief Technology Officer</h3><small>Brookline Railway</small>
  </div>
  <div class="voices-arrows">
    <svg width="30" height="14" viewBox="0 0 30 14"><path d="M29 7H3M9 1L3 7l6 6" fill="none" stroke="#fff" stroke-width="2"/></svg>
    <svg width="30" height="14" viewBox="0 0 30 14"><path d="M1 7h26M21 1l6 6-6 6" fill="none" stroke="#fff" stroke-width="2"/></svg>
  </div>
</section>

<section class="section lead">
  <div class="lead-circle"></div>
  <div class="lead-photo" role="img" aria-label="Photo of a laptop showing a video meeting"></div>
  <form class="form-card">
    <div class="form-head">
      <h2>Ready To Start Migrating?</h2>
      <p>Speak With One Of Our Expert Engineers About Your Business Goals</p>
    </div>
    <div class="field">First Name</div>
    <div class="field">Last Name</div>
    <div class="field">Company Name</div>
    <div class="field">Email</div>
    <div class="field">Phone</div>
    <div class="field">Title</div>
    <a class="btn" href="#">Talk with an Expert Today!</a>
  </form>
</section>

<footer class="section footer">
  <div class="col" style="left:171px">
    <h3>Services Offered</h3>
    <ul>
      <li>Tessory Mail Migration</li>
      <li>Relaymark Server Migration</li>
      <li>Halvo Workplace Migration</li>
      <li>PST File Configurations</li>
      <li>Ferrow Notes Migration</li>
      <li>IMAP</li>
      <li>Legacy Archive Migration</li>
    </ul>
  </div>
  <div class="col" style="left:392px">
    <h3>Connect Us</h3>
    <p>Halden Ridge Consulting, LLC<br>418 Corrin Loop, Suite 210<br>Larkfield, WY 82990<br>Toll-Free: (877) 555-0148<br>Email:<br>hello@DesksetShiftCrew.com</p>
  </div>
  <div class="col" style="left:682px">
    <h3>Contact Form</h3>
    <div class="mini-field">NAME</div>
    <div class="mini-field">EMAIL</div>
    <div class="mini-field">PHONE</div>
    <div class="mini-field">MESSAGE</div>
    <span class="mini-send">SEND</span>
  </div>
  <p class="copyright">2018 Copyright - DesksetShiftCrew.com - Halden Ridge Consulting, LLC<br>All product and company names are trademarks or registered trademarks of<br>their respective holders. Use of them does not imply any affiliation with or endorsement by them.</p>
</footer>

</body>
</html>
```